Concierge Healthcare Business Card Design and Logo

We need a logo and business card design for a new company called "Sound Keeper". We will provide concierge audiological care, hearing aids, hearing exams, custom hearing protection etc to patients in the comfort of their homes and offices. We would like a sleek and modern design preferably with an Ear related logo.

Target Market(s)

People with hearing loss, Hunters, Musicians
My usual clientele are older individuals so usually 50+ years old

Industry/Entity Type

Health Care

Contact Information for Business Card

Clara Whitfield, AuD
Audiologist
512-418-2967
soundkeeper@mailvista.net
www.soundkeeperclinic.net

Logo Text

Sound Keeper

Number of Pages Required

3 page

```html
<!DOCTYPE html>
<html lang="en">
<head>
<meta charset="utf-8">
<title>Sound Keeper – Business Card</title>
<link href="https://fonts.googleapis.com/css2?family=Lato:wght@400;700&display=swap" rel="stylesheet">
<style>
  :root {
    --backdrop: #1f2021;
    --card: #4a4c4e;
    --ink: #cfd0d1;
    --ink-soft: #b9babb;
    --rule: #8e9092;
  }
  html, body {
    margin: 0;
    width: 1200px;
    height: 900px;
    overflow: hidden;
    background: var(--backdrop);
  }
  .business-card {
    position: absolute;
    left: 180px;
    top: 210px;
    width: 840px;
    height: 480px;
    background: var(--card);
    border-radius: 4px;
    font-family: "Lato", sans-serif;
    color: var(--ink);
  }
  .brand {
    position: absolute;
    left: 0;
    top: 0;
    width: 430px;
    height: 100%;
    display: flex;
    flex-direction: column;
    align-items: center;
    justify-content: center;
    gap: 26px;
  }
  .brand-dot {
    width: 92px;
    height: 92px;
    border-radius: 50%;
    background: var(--ink);
  }
  .brand-name {
    font-size: 31px;
    font-weight: 400;
    letter-spacing: 0.12em;
    text-transform: uppercase;
    margin: 0;
  }
  .divider {
    position: absolute;
    left: 440px;
    top: 110px;
    width: 2px;
    height: 270px;
    background: var(--rule);
  }
  .contact {
    position: absolute;
    left: 490px;
    top: 140px;
  }
  .person-name {
    margin: 0;
    font-size: 22px;
    font-weight: 700;
    letter-spacing: 0.03em;
    text-transform: uppercase;
  }
  .person-title {
    margin: 2px 0 30px;
    font-size: 18px;
    color: var(--ink-soft);
  }
  .contact-list {
    list-style: none;
    margin: 0;
    padding: 0;
    font-size: 19px;
    line-height: 1.35;
    letter-spacing: 0.02em;
  }
</style>
</head>
<body>
  <main class="business-card">
    <section class="brand">
      <div class="brand-dot"></div>
      <h1 class="brand-name">Sound Keeper</h1>
    </section>
    <div class="divider"></div>
    <section class="contact">
      <h2 class="person-name">Clara Whitfield, AuD</h2>
      <p class="person-title">Audiologist</p>
      <ul class="contact-list">
        <li class="phone">512-418-2967</li>
        <li class="email">soundkeeper@mailvista.net</li>
        <li class="website">www.soundkeeperclinic.net</li>
      </ul>
    </section>
  </main>
</body>
</html>
```